Bellhaven Select Business Card Design Project

About the company: Here at Marigrove Essence, we focus on cosmetic products that based on essential oils and different kinds of plant essences. All of our raw materials are pure organic and specially selected from local producers in Australia.

I'm here to look for a unique business card design, to replace the current one later on, so I don't have many requirements. Why I wanna restrict designers' creativity?

All I know is: 1. do not make it too complicated, straight forward, simple and pure. 2. this design may be used for other purposes (i.e. logo and slogan on the front, Brand Story and contact details at the back). Therefor, I'd like to have the design for 3 layouts, one only have logo, slogan, contact detials, one for the brand story, the other one for the personal business card with staff's mob etc...

A vector graphic is required, i.e. eps, ai, easy for me to resize.

Round Corner.

Thanks
Updates

Plz add "Hand made in Australia" in the design, cheers.

Target Market(s)

Women aged yr 20-50

Industry/Entity Type

Business

Requirements
Must have
• Logo: please see attacment (eps, ai)

Slogan: Dew Touched Delight

Website:www.marigroveessence-demo.com.au

Address: temporary not available

Phone: temporary not available

"Hand made in Australia"

Nice to have
• Prefer round corner

```html
<!DOCTYPE html>
<html lang="en">
<head>
<meta charset="utf-8">
<title>Marigrove Essence – Business Card</title>
<link rel="stylesheet" href="https://fonts.googleapis.com/css2?family=PT+Sans:wght@400;700&family=Cinzel:wght@400&display=swap">
<style>
  :root {
    --stage: #8c8c8c;
    --card: #5d5d5d;
    --card-edge: #2e2e2e;
    --band: #4a4a4a;
    --band-light: #6a6a6a;
    --accent: #ec6a82;
    --accent-line: #f7c4cd;
    --ink: #ffffff;
    --ink-soft: #ececec;
  }
  * { box-sizing: border-box; margin: 0; padding: 0; }
  html, body {
    width: 1200px; height: 739px; overflow: hidden;
    background: var(--stage);
  }
  .card {
    position: absolute; left: 93px; top: 76px;
    width: 1014px; height: 586px;
    background: var(--card);
    border: 2px solid var(--card-edge);
    overflow: hidden;
    font-family: "PT Sans", Arial, sans-serif;
    color: var(--ink);
  }
  .card__band {
    position: absolute; left: 0; top: 0;
    width: 954px; height: 586px;
  }
  .card__stripe {
    position: absolute; top: 0; right: 0;
    width: 56px; height: 100%;
    background: var(--accent);
  }
  .card__stripe::before {
    content: ""; position: absolute; top: 0; left: 8px;
    width: 3px; height: 100%;
    background: var(--accent-line);
  }
  .content {
    position: absolute; left: 0; top: 0;
    width: 958px; height: 100%;
    text-align: center;
  }
  .brand {
    position: absolute; left: 0; right: 0; top: 48px;
    font-size: 78px; font-weight: 400; line-height: 1;
    color: var(--accent); letter-spacing: 2px;
  }
  .brand__mark {
    position: absolute; left: 450px; top: 150px;
    width: 48px; height: 48px; border-radius: 50%;
    background: var(--accent);
  }
  .slogan {
    position: absolute; left: 0; right: 0; top: 252px;
    font-family: "Cinzel", "Times New Roman", serif;
    font-size: 30px; letter-spacing: 5px;
    color: var(--ink-soft);
  }
  .about {
    position: absolute; left: 0; right: 0; top: 346px;
  }
  .about__title {
    font-size: 30px; font-weight: 700; line-height: 1.1;
  }
  .about__text {
    margin-top: 2px;
    font-size: 24.5px; line-height: 30px;
    color: var(--ink-soft);
  }
  .contact {
    position: absolute; left: 0; right: 0; top: 494px;
    display: flex; justify-content: center; align-items: center; gap: 26px;
    font-size: 27px;
  }
  .contact__item { display: flex; align-items: center; gap: 8px; }
  .contact__icon { width: 20px; height: 24px; fill: var(--ink); }
  .website {
    position: absolute; left: 0; right: 0; top: 536px;
    font-size: 26px; color: var(--ink-soft);
  }
</style>
</head>
<body>
  <main class="card">
    <svg class="card__band" viewBox="0 0 954 586" aria-hidden="true">
      <defs>
        <linearGradient id="bandShade" x1="0" y1="0" x2="0" y2="1">
          <stop offset="0" stop-color="#777777"/>
          <stop offset="0.18" stop-color="#555555"/>
          <stop offset="1" stop-color="#4a4a4a"/>
        </linearGradient>
      </defs>
      <path d="M0 392 Q477 250 954 392 L954 586 L0 586 Z" fill="url(#bandShade)"/>
    </svg>
    <div class="card__stripe"></div>

    <section class="content">
      <h1 class="brand">Marigrove</h1>
      <span class="brand__mark" aria-hidden="true"></span>
      <p class="slogan">Dew Touched Delight</p>

      <div class="about">
        <h2 class="about__title">About the company:</h2>
        <p class="about__text">
          Here at Marigrove Essence, we focus on cosmetic products that based on<br>
          essential oils and different kinds of plant essences. All of our raw materials are<br>
          pure organic and specially selected from local producers in Australia.
        </p>
      </div>

      <div class="contact">
        <span class="contact__item">
          <svg class="contact__icon" viewBox="0 0 20 24" aria-hidden="true">
            <path d="M4 2 L8 2 L9 8 L6.5 9.5 Q8 15 12.5 18 L14.5 15.5 L19 17 L18.5 21.5 Q17 23 14 22 Q4 18 1.5 6 Q1.5 3 4 2 Z"/>
          </svg>
          123-456-7890
        </span>
        <span class="contact__item">
          <svg class="contact__icon" viewBox="0 0 20 24" aria-hidden="true">
            <path d="M5 1 H15 Q17 1 17 3 V21 Q17 23 15 23 H5 Q3 23 3 21 V3 Q3 1 5 1 Z M5.5 4 V14 H14.5 V4 Z M6 16 H8 V18 H6 Z M9 16 H11 V18 H9 Z M12 16 H14 V18 H12 Z M6 19 H8 V21 H6 Z M9 19 H11 V21 H9 Z M12 19 H14 V21 H12 Z"/>
          </svg>
          123-456-7890
        </span>
        <span class="contact__item">Street name, City, State, zip code</span>
      </div>

      <p class="website">www.marigroveessence-demo.com.au</p>
    </section>
  </main>
</body>
</html>
```